Wattle Groundworks Flyer

I would like to purchase a customized version of a design you have previously submitted - https://www.artpitchhub.net/design/8843290
Hello,
I like this design a lot. I would change the bullet points to;
- Landscape Design & Construction
- Paver Patio/path installations
- Retaining wall installations
- Pergola Installations
- Grading
- All Hardscape construction
- Drainage specialist
- Yard Maintenance plans
- Mulch & Pine needles
- Rooted Fine Service!
In the yellow star part - "Mention this flyer for a 10% discount!"
Phone number - 7045182409
email - wattlegroundworks@mailzen.net
website - www.wattlegroundworks.net
Target Market(s)
Residential homes in Charlotte, North Carolina
Industry/Entity Type
Landscaping
Look and feel
Each slider illustrates characteristics of the customer's brand and the style your logo design should communicate.

```html
<!DOCTYPE html>
<html lang="en">
<head>
<meta charset="utf-8">
<title>Wattle Groundworks Flyer</title>
<link rel="stylesheet" href="https://fonts.googleapis.com/css2?family=Anton&family=Bitter:wght@500;700&display=swap">
<style>
  :root {
    --brown: #a5622c;
    --brown-light: #c17a3c;
    --dark: #241913;
    --paper: #ecebe8;
    --ink: #1c1512;
    --white: #ffffff;
  }
  * { margin: 0; padding: 0; box-sizing: border-box; }
  html, body { width: 846px; height: 1200px; overflow: hidden; background: var(--paper); }
  .flyer { position: relative; width: 846px; height: 1200px; overflow: hidden; font-family: "Bitter", serif; color: var(--ink); }
  .flyer-art { position: absolute; inset: 0; }

  .brand { position: absolute; left: 44px; top: 70px; display: flex; align-items: center; gap: 12px; }
  .brand-dot { width: 34px; height: 34px; border-radius: 50%; background: var(--brown); flex: none; }
  .brand-name { font-family: "Bitter", serif; font-weight: 700; font-size: 30px; line-height: 1.1; color: var(--brown); }

  .headline { position: absolute; left: 418px; top: 30px; font-family: "Anton", sans-serif; font-size: 48px; line-height: 58px; color: var(--ink); letter-spacing: 0.5px; }
  .headline .accent { color: var(--brown); display: block; }

  .services { position: absolute; left: 52px; top: 650px; }
  .services-title { font-family: "Bitter", serif; font-weight: 700; font-size: 36px; color: var(--ink); margin-left: 30px; letter-spacing: 0.5px; }
  .services-rule { width: 380px; height: 3px; background: var(--brown); margin: 4px 0 18px -52px; }
  .services-list { list-style: none; }
  .services-list li { display: flex; align-items: center; gap: 12px; font-weight: 500; font-size: 20px; height: 39.5px; color: var(--ink); }
  .tick { width: 16px; height: 16px; flex: none; }

  .offer { position: absolute; left: 600px; top: 927px; width: 200px; height: 200px; display: flex; flex-direction: column; align-items: center; justify-content: center; font-family: "Anton", sans-serif; color: var(--white); text-align: center; line-height: 1.05; }
  .offer-small { font-size: 19px; }
  .offer-big { font-size: 38px; margin: 4px 0 2px; }
  .offer-end { font-size: 19px; }

  .contact-bar { position: absolute; left: 0; right: 0; bottom: 0; height: 68px; display: flex; align-items: center; justify-content: center; gap: 26px; color: var(--white); font-size: 15px; font-family: "Bitter", serif; font-weight: 500; }
  .contact-item { display: flex; align-items: center; gap: 8px; }
  .contact-icon { width: 20px; height: 20px; flex: none; }
</style>
</head>
<body>
<main class="flyer">
  <svg class="flyer-art" width="846" height="1200" viewBox="0 0 846 1200" xmlns="http://www.w3.org/2000/svg">
    <defs>
      <linearGradient id="paperGrad" x1="0" y1="0" x2="1" y2="1">
        <stop offset="0" stop-color="#f3f2f0"/>
        <stop offset="1" stop-color="#d9d7d3"/>
      </linearGradient>
      <linearGradient id="gardenGrad" x1="0" y1="0" x2="1" y2="1">
        <stop offset="0" stop-color="#3f6b2a"/>
        <stop offset="0.35" stop-color="#5f9a34"/>
        <stop offset="0.6" stop-color="#8a4a3a"/>
        <stop offset="1" stop-color="#4e8a2c"/>
      </linearGradient>
      <linearGradient id="pavingGrad" x1="0" y1="0" x2="1" y2="1">
        <stop offset="0" stop-color="#c9c7c2"/>
        <stop offset="0.6" stop-color="#9c9a95"/>
        <stop offset="1" stop-color="#6f7368"/>
      </linearGradient>
      <linearGradient id="fadeGrad" x1="0" y1="0" x2="1" y2="0">
        <stop offset="0" stop-color="#ffffff" stop-opacity="0.95"/>
        <stop offset="0.6" stop-color="#ffffff" stop-opacity="0.75"/>
        <stop offset="1" stop-color="#ffffff" stop-opacity="0"/>
      </linearGradient>
      <linearGradient id="crewGrad" x1="0" y1="0" x2="0" y2="1">
        <stop offset="0" stop-color="#8c8a84"/>
        <stop offset="0.45" stop-color="#4aa6cf"/>
        <stop offset="1" stop-color="#6f9a3e"/>
      </linearGradient>
    </defs>

    <rect class="paper" width="846" height="1200" fill="url(#paperGrad)"/>

    <rect class="paving-photo" role="img" aria-label="Photo of grey paving stones with a fallen autumn leaf" x="0" y="560" width="846" height="580" fill="url(#pavingGrad)"/>
    <rect class="services-fade" x="0" y="560" width="600" height="580" fill="url(#fadeGrad)"/>

    <path class="garden-photo" role="img" aria-label="Photo of a landscaped garden with flower beds, shrubs and lawn"
      d="M0,236 C170,200 330,330 500,332 C660,334 770,240 846,196 L846,760 C780,700 700,640 560,612 C380,578 160,600 0,672 Z"
      fill="url(#gardenGrad)"/>

    <path class="garden-edge" d="M0,236 C170,200 330,330 500,332 C660,334 770,240 846,196" fill="none" stroke="#ffffff" stroke-width="5"/>
    <path class="garden-band" d="M300,280 C380,322 450,338 520,336 C660,330 770,250 846,200 L846,182 C760,232 660,312 520,318 C450,320 380,308 300,280 Z" fill="var(--brown)"/>

    <path class="services-swoop" d="M0,655 C150,590 360,570 560,600 C380,590 170,620 0,720 Z" fill="var(--dark)"/>
    <path class="services-swoop-line" d="M0,640 C150,575 360,558 560,592" fill="none" stroke="var(--brown)" stroke-width="4"/>

    <circle class="crew-ring" cx="622" cy="722" r="160" fill="var(--brown)"/>
    <circle class="crew-ring-inner" cx="622" cy="722" r="151" fill="#ffffff"/>
    <circle class="crew-photo" role="img" aria-label="Photo of two landscapers planting shrubs outside a building" cx="622" cy="722" r="146" fill="url(#crewGrad)"/>

    <line class="tag-string" x1="700" y1="860" x2="700" y2="932" stroke="#3a2a20" stroke-width="2"/>
    <circle class="offer-badge" cx="700" cy="1027" r="100" fill="var(--brown)" stroke="var(--dark)" stroke-width="4"/>
    <circle class="offer-stitch" cx="700" cy="1027" r="88" fill="none" stroke="#ffffff" stroke-width="2" stroke-dasharray="6 5"/>
    <circle class="offer-hole" cx="700" cy="940" r="6" fill="#ffffff" stroke="var(--dark)" stroke-width="2"/>

    <path class="footer-line" d="M0,1122 C300,1112 600,1110 846,1096" fill="none" stroke="var(--brown)" stroke-width="5"/>
    <path class="footer-band" d="M0,1130 C300,1120 600,1118 846,1104 L846,1200 L0,1200 Z" fill="var(--dark)"/>
  </svg>

  <div class="brand">
    <span class="brand-dot"></span>
    <span class="brand-name">Wattle<br>Groundworks</span>
  </div>

  <h1 class="headline">WHERE ‘BLOOMIN’<span class="accent">GREAT SERVICE</span>HAPPENS DAILY!</h1>

  <section class="services">
    <h2 class="services-title">SERVICES</h2>
    <div class="services-rule"></div>
    <ul class="services-list">
      <li><svg class="tick" viewBox="0 0 16 16"><circle cx="8" cy="8" r="8" fill="#a5622c"/><path d="M4.5 8.3l2.4 2.3 4.6-4.8" fill="none" stroke="#fff" stroke-width="2"/></svg>Landscape Design &amp; Construction</li>
      <li><svg class="tick" viewBox="0 0 16 16"><circle cx="8" cy="8" r="8" fill="#a5622c"/><path d="M4.5 8.3l2.4 2.3 4.6-4.8" fill="none" stroke="#fff" stroke-width="2"/></svg>Paver Patio/path installations</li>
      <li><svg class="tick" viewBox="0 0 16 16"><circle cx="8" cy="8" r="8" fill="#a5622c"/><path d="M4.5 8.3l2.4 2.3 4.6-4.8" fill="none" stroke="#fff" stroke-width="2"/></svg>Retaining wall installations</li>
      <li><svg class="tick" viewBox="0 0 16 16"><circle cx="8" cy="8" r="8" fill="#a5622c"/><path d="M4.5 8.3l2.4 2.3 4.6-4.8" fill="none" stroke="#fff" stroke-width="2"/></svg>Pergola Installations</li>
      <li><svg class="tick" viewBox="0 0 16 16"><circle cx="8" cy="8" r="8" fill="#a5622c"/><path d="M4.5 8.3l2.4 2.3 4.6-4.8" fill="none" stroke="#fff" stroke-width="2"/></svg>Grading</li>
      <li><svg class="tick" viewBox="0 0 16 16"><circle cx="8" cy="8" r="8" fill="#a5622c"/><path d="M4.5 8.3l2.4 2.3 4.6-4.8" fill="none" stroke="#fff" stroke-width="2"/></svg>All Hardscape construction</li>
      <li><svg class="tick" viewBox="0 0 16 16"><circle cx="8" cy="8" r="8" fill="#a5622c"/><path d="M4.5 8.3l2.4 2.3 4.6-4.8" fill="none" stroke="#fff" stroke-width="2"/></svg>Drainage specialist</li>
      <li><svg class="tick" viewBox="0 0 16 16"><circle cx="8" cy="8" r="8" fill="#a5622c"/><path d="M4.5 8.3l2.4 2.3 4.6-4.8" fill="none" stroke="#fff" stroke-width="2"/></svg>Yard Maintenance plans</li>
      <li><svg class="tick" viewBox="0 0 16 16"><circle cx="8" cy="8" r="8" fill="#a5622c"/><path d="M4.5 8.3l2.4 2.3 4.6-4.8" fill="none" stroke="#fff" stroke-width="2"/></svg>Mulch &amp; Pine needles</li>
      <li><svg class="tick" viewBox="0 0 16 16"><circle cx="8" cy="8" r="8" fill="#a5622c"/><path d="M4.5 8.3l2.4 2.3 4.6-4.8" fill="none" stroke="#fff" stroke-width="2"/></svg>Rooted Fine Service!</li>
    </ul>
  </section>

  <div class="offer">
    <span class="offer-small">MENTION</span>
    <span class="offer-small">THIS FLYER FOR A</span>
    <span class="offer-big">10%</span>
    <span class="offer-end">DISCOUNT!</span>
  </div>

  <footer class="contact-bar">
    <span class="contact-item">
      <svg class="contact-icon" viewBox="0 0 20 20"><circle cx="10" cy="10" r="10" fill="#a5622c"/><path d="M7 5.5c-.8.4-1.3 1.3-1 2.4.8 2.8 3.3 5.3 6.1 6.1 1.1.3 2-.2 2.4-1l-1.8-1.6-1.2.8c-1.3-.6-2.6-1.9-3.2-3.2l.8-1.2z" fill="#fff"/></svg>
      7045182409
    </span>
    <span class="contact-item">
      <svg class="contact-icon" viewBox="0 0 20 20"><circle cx="10" cy="10" r="10" fill="#a5622c"/><rect x="5" y="6.5" width="10" height="7" rx="1" fill="none" stroke="#fff" stroke-width="1.4"/><path d="M5.3 7l4.7 3.6L14.7 7" fill="none" stroke="#fff" stroke-width="1.4"/></svg>
      wattlegroundworks@mailzen.net
    </span>
    <span class="contact-item">
      <svg class="contact-icon" viewBox="0 0 20 20"><circle cx="10" cy="10" r="10" fill="#a5622c"/><circle cx="10" cy="10" r="5" fill="none" stroke="#fff" stroke-width="1.3"/><path d="M5 10h10M10 5c-2.2 2.8-2.2 7.2 0 10M10 5c2.2 2.8 2.2 7.2 0 10" fill="none" stroke="#fff" stroke-width="1.1"/></svg>
      www.wattlegroundworks.net
    </span>
  </footer>
</main>
</body>
</html>
```